Raw Material for Personal Care Products

We need to make a brochure with the products we sell to manufacture natural personal care products

Target Market(s)

Cosmetics Manufacturers

Industry/Entity Type

Cosmetics

Colors
00AB8E
00BBA5
67D7C9
C6EFE9
E9F9F6

Requirements
Must have
• Images associated with nature, organics
Should not have
• Chemicals industries, refinaries

```html
<!DOCTYPE html>
<html lang="es">
<head>
<meta charset="UTF-8">
<title>Materias Primas Naturales Orgánicas para Cuidado Personal</title>
<link href="https://fonts.googleapis.com/css2?family=Jost:wght@400;600;700&display=swap" rel="stylesheet">
<style>
  :root {
    --green-dark: #1f7a36;
    --green-panel: #c3de99;
    --white: #ffffff;
    --photo-light: #e6e1dc;
    --photo-warm: #cfc6bf;
    --marble: #eeeeec;
    --marble-shade: #dcdcda;
  }
  * { margin: 0; padding: 0; box-sizing: border-box; }
  html, body { width: 927px; height: 1200px; overflow: hidden; background: var(--white); }
  body { font-family: "Jost", sans-serif; color: var(--green-dark); }
  .sheet { position: relative; width: 927px; height: 1200px; overflow: hidden; background: var(--white); }

  .title {
    position: absolute; left: 64px; top: 48px;
    font-size: 30px; line-height: 36px; font-weight: 700; color: var(--green-dark);
  }
  .brand {
    position: absolute; left: 760px; top: 70px; width: 130px;
    display: flex; align-items: center; gap: 8px;
    font-size: 20px; font-weight: 700; color: var(--green-dark); letter-spacing: 0.5px;
  }
  .brand-mark { width: 14px; height: 14px; background: var(--green-dark); flex: none; }

  .backdrop {
    position: absolute; left: 0; top: 153px; width: 927px; height: 912px;
    background: linear-gradient(160deg, var(--photo-light) 0%, var(--photo-warm) 55%, #bdb7b0 100%);
  }
  .marble {
    position: absolute; left: 607px; top: 374px; width: 320px; height: 517px;
    background: linear-gradient(200deg, var(--marble) 0%, #f5f5f3 50%, var(--marble-shade) 100%);
  }

  .panel { position: absolute; left: 0; width: 574px; background: var(--green-panel); }
  .panel-oils { top: 224px; height: 358px; }
  .panel-surf { top: 651px; height: 380px; }

  .tab {
    position: absolute; left: 33px; background: var(--white);
    font-size: 21px; font-weight: 700; color: var(--green-dark);
    display: flex; align-items: center; padding-left: 31px;
  }
  .tab-oils { top: 182px; width: 387px; height: 71px; }
  .tab-surf { top: 607px; width: 331px; height: 71px; padding-left: 34px; }

  .list { position: absolute; list-style: none; font-size: 17.5px; line-height: 18.2px; color: var(--green-dark); }
  .col-a { left: 67px; top: 277px; }
  .col-b { left: 309px; top: 277px; }
  .note { position: absolute; left: 33px; top: 540px; font-size: 16.5px; }

  .group-title { position: absolute; left: 67px; font-size: 17px; font-weight: 600; }
  .amino-title { top: 700px; }
  .gluco-title { top: 852px; }
  .amino-list { left: 67px; top: 727px; }
  .gluco-list { left: 67px; top: 879px; }

  .card { position: absolute; left: 590px; width: 337px; background: var(--white); text-align: center; font-size: 15px; line-height: 18.2px; }
  .card-frag { top: 723px; height: 104px; padding-top: 38px; }
  .card-cert { top: 891px; height: 140px; padding-top: 50px; padding-left: 26px; }
  .label {
    position: absolute; background: var(--green-panel);
    display: flex; align-items: center; justify-content: center;
    font-size: 21px; font-weight: 700; letter-spacing: 0.3px;
  }
  .label-frag { left: 657px; top: 680px; width: 203px; height: 70px; }
  .label-cert { left: 634px; top: 849px; width: 249px; height: 71px; }

  .contact-head { position: absolute; left: 67px; top: 1092px; font-size: 20px; font-weight: 600; }
  .phone { position: absolute; left: 67px; top: 1130px; font-size: 21px; font-weight: 700; letter-spacing: 0.5px; }
  .address { position: absolute; right: 69px; top: 1128px; font-size: 20px; }
</style>
</head>
<body>
<div class="sheet">
  <h1 class="title">Materias Primas Naturales Orgánicas<br>para Cuidado Personal</h1>
  <div class="brand"><span class="brand-mark"></span>VERDANTA</div>

  <div class="backdrop" role="img" aria-label="Fotografía de cepillos de bambú y jabón natural sobre mármol"></div>
  <div class="marble" role="img" aria-label="Fotografía de una rama de tomillo fresco sobre mármol blanco"></div>

  <div class="panel panel-oils"></div>
  <div class="tab tab-oils">Aceites y Mantecas Naturales</div>
  <ul class="list col-a">
    <li>Aceite de Acaí</li><li>Aceite de Aguacate</li><li>Aceite de Almendra Dulce</li>
    <li>Aceite de Andiroba</li><li>Aceite de Argán</li><li>Aceite de Avellana</li>
    <li>Aceite de Babacu</li><li>Aceite de Buriti</li><li>Aceite de Castor</li>
    <li>Aceite de Coco</li><li>Aceite de de Nuez</li><li>Aceite de Girasol</li>
    <li>Aceite de Jojoba</li>
  </ul>
  <ul class="list col-b">
    <li>Aceite de Macadamia</li><li>Aceite de Oliva</li><li>Aceite de Pracaxi</li>
    <li>Aceite de Semilla de Durazno</li><li>Aceite de Semilla de Uva</li><li>Aceite de Sesamo</li>
    <li>Aceite de Soya</li><li>Aceite de Zanahoria</li><li>Manteca de Cupuacu</li>
    <li>Manteca de Karite</li><li>Manteca de Murumuru</li><li>Manteca de Ucuba</li>
    <li>Scrub de Murumuru</li>
  </ul>
  <p class="note">Los Aceites están disponibles Vírgenes, Refinados, desodorizados,</p>

  <div class="panel panel-surf"></div>
  <div class="tab tab-surf">Surfactantes Naturales</div>
  <h3 class="group-title amino-title">Surfactante Amino Acido</h3>
  <ul class="list amino-list">
    <li>Glicinato de Potasio Cocoil y Glicerina</li><li>Glicinato de Potasio Cocoil</li>
    <li>Glicinato de Sodio Cocoil y Glicerina</li><li>Glicinato de Sodio Cocoil</li>
    <li>Glutamato de Sodio Cocoil</li>
  </ul>
  <h3 class="group-title gluco-title">Sufactante Alquil Glucosido</h3>
  <ul class="list gluco-list">
    <li>Glucosido Laurico</li><li>Glucosido de Coco</li><li>Glucosido Decilico</li>
    <li>Hidroxipropil Sulfonato Laurilglucosido de Sodio</li>
    <li>Carboxilato Glucosa Laurico de Sodio y Glucosido Laurico</li>
    <li>Cocoil Isetianato de Sodio (SCI)</li><li>CocoamidoPropilBetaine (CAPB)</li>
  </ul>

  <div class="card card-frag">Fragancias Convencionales<br>Fragancias Naturales 100% (FLORAVIVA)</div>
  <div class="label label-frag">FRAGANCIAS</div>

  <div class="card card-cert">Terracert (Organic Farming Product)<br>Orbis Organic<br>Kosher (Kashrut Council)<br>Agro Organic Standard</div>
  <div class="label label-cert">CERTIFICACIONES</div>

  <p class="contact-head">Contact Us</p>
  <p class="phone">123–456–789</p>
  <p class="address">Anywhere St. City</p>
</div>
</body>
</html>
```